LEARN Business Skills so you can Earn a good living

size of the poster is 8”x 10.75" plus 0.25" bleed.
Please leave 1 inch on the bottoum for footer
I want a design a poster that will attract people's attention.
I appreciate a creative ad however the ad should not take away from being able to clearly read the text.
-I also appreciate a simple creative ad that is not too busy.
-you can use graphics, vectors, or pictures of real people.
-however, if you use real people it should be a white male that is wearing a white shirt and look like a professional person.

Target Market(s)

Potential young business people

Industry/Entity Type

education

Requirements
Must have
• easy to read the text
Nice to have
• I would like a "creative" simple ad that is easy to be read
Should not have
• pictures of women

```html
<!DOCTYPE html>
<html lang="en">
<head>
<meta charset="utf-8">
<title>Learn It to Earn It – Business Enrichment Course</title>
<link href="https://fonts.googleapis.com/css2?family=Bebas+Neue&display=swap" rel="stylesheet">
<style>
  :root {
    --green-bright: #1f9a3f;
    --green-mid: #0d6a27;
    --green-deep: #032a0e;
    --title-white: #f2f2f2;
    --accent-yellow: #ffee00;
    --body-white: #ffffff;
    --panel-fill: rgba(0, 30, 8, 0.28);
    --panel-line: rgba(255, 255, 255, 0.45);
    --chart-tint: rgba(120, 200, 140, 0.13);
  }
  html, body {
    margin: 0;
    padding: 0;
    overflow: hidden;
    background: #0a3a16;
  }
  .poster {
    position: relative;
    width: 907px;
    height: 1200px;
    overflow: hidden;
    background: radial-gradient(ellipse 110% 75% at 60% 10%, var(--green-bright) 0%, var(--green-mid) 45%, var(--green-deep) 100%);
    font-family: "Bebas Neue", "Arial Narrow", sans-serif;
  }
  .growth-chart {
    position: absolute;
    inset: 0;
  }
  .figure-area {
    position: absolute;
    left: 590px;
    top: 60px;
    width: 300px;
    height: 1095px;
    border-radius: 140px 140px 40px 40px;
    background: linear-gradient(180deg, rgba(110, 200, 130, 0.28) 0%, rgba(60, 150, 85, 0.18) 55%, rgba(20, 80, 40, 0.12) 100%);
  }
  .headline {
    position: absolute;
    left: 56px;
    top: 57px;
    margin: 0;
    color: var(--title-white);
    font-weight: 400;
    font-size: 174px;
    line-height: 149px;
    letter-spacing: 1px;
  }
  .headline .connector-word {
    position: absolute;
    left: 480px;
    top: 8px;
    color: var(--accent-yellow);
    font-size: 57px;
    line-height: 57px;
    letter-spacing: 0;
  }
  .info-panel {
    position: absolute;
    left: 56px;
    box-sizing: border-box;
    border: 1.5px solid var(--panel-line);
    border-radius: 16px;
    background: var(--panel-fill);
    color: var(--body-white);
  }
  .info-panel--intro {
    top: 373px;
    width: 560px;
    height: 284px;
    padding: 16px 0 0 30px;
  }
  .info-panel--subjects {
    top: 745px;
    width: 628px;
    height: 347px;
    padding: 24px 0 0 30px;
  }
  .panel-link {
    position: absolute;
    left: 128px;
    top: 657px;
    width: 1.5px;
    height: 88px;
    background: var(--panel-line);
  }
  .panel-heading {
    margin: 0;
    color: var(--accent-yellow);
    font-weight: 400;
    font-size: 43px;
    line-height: 44px;
    letter-spacing: 0.6px;
  }
  .panel-heading + .panel-text + .panel-heading {
    margin-top: 8px;
  }
  .panel-text {
    margin: 0 0 10px;
    font-size: 27px;
    line-height: 38px;
    letter-spacing: 1.2px;
  }
  .subject-list {
    list-style: none;
    margin: 0;
    padding: 0;
    font-size: 27px;
    line-height: 37.5px;
    letter-spacing: 1.2px;
  }
  .subject-list li {
    white-space: pre;
  }
</style>
</head>
<body>
  <main class="poster">
    <svg class="growth-chart" width="907" height="1200" viewBox="0 0 907 1200" aria-hidden="true">
      <rect x="222" y="667" width="82" height="533" fill="var(--chart-tint)"/>
      <rect x="319" y="533" width="76" height="667" fill="var(--chart-tint)"/>
      <rect x="445" y="311" width="76" height="889" fill="var(--chart-tint)"/>
    </svg>

    <div class="figure-area" role="img" aria-label="Faint silhouette of a businessman climbing up a rising bar chart"></div>

    <h1 class="headline">LEARN IT<span class="connector-word">TO</span><br>EARN IT</h1>

    <section class="info-panel info-panel--intro">
      <h2 class="panel-heading">Business Enrichment Course</h2>
      <p class="panel-text">A proven success of helping people<br>in their livelihoods</p>
      <h2 class="panel-heading">Business skills that will help you:</h2>
      <p class="panel-text">Get a quality job - Start<br>Grow your businessIncrease your salary</p>
    </section>

    <div class="panel-link"></div>

    <section class="info-panel info-panel--subjects">
      <ul class="subject-list"><li>Business Admiistration – Small Business Management</li><li>Finance - Investments - Computers- Accounting</li><li>Sales - Marketing</li><li>Project Management Interviewing Skills</li><li>Business Law -Negotiation – Public Speaking</li><li>Import/Export - Information Technoloy</li><li>Distribution - Marketing -   Ledgerly</li><li>Real Estate - Health Care-Management - Shopwave</li></ul>
    </section>
  </main>
</body>
</html>
```